Cafe Opening Flyer Design Project

We need a flyer for the grand opening of our new cafe. It should appeal very much to our target consumer - working adults within the CBD area, where there is substantial competition as well.

Keep the message clear to the audience:
(below statements are just examples, please be creative and come up with your own phrases)
1. there's a new cafe you don't wanna miss out..
2. and coffee is always a good idea..

Be bold and creative!
Updates

Dear designers,

Kindly add in our opening hours on the flyer (A5 size, single side)
Weekdays: 7am to 6pm
Sat: 8am to 3pm
Closed on Sun & PH

Thank you!

Target Market(s)

Working adults in the CBD area, coffee lovers

Industry/Entity Type

Cafe

Requirements
Must have
• Location:
24 Brindlemere Wharf, The Linden Court #03-18

```html
<!DOCTYPE html>
<html lang="en">
<head>
<meta charset="utf-8">
<title>Kindly Brewed – Grand Opening</title>
<link href="https://fonts.googleapis.com/css2?family=Saira+Condensed:wght@400;500;600&family=Arimo:wght@400;700&display=swap" rel="stylesheet">
<style>
  :root {
    --paper: #ebe8e3;
    --coral: #fa6258;
    --ink: #111111;
    --tan: #c39a66;
    --steel-light: #d2d0cc;
    --steel-dark: #5e5a56;
  }
  html, body {
    margin: 0;
    padding: 0;
    overflow: hidden;
    background: var(--paper);
  }
  .flyer {
    position: relative;
    width: 846px;
    height: 1200px;
    overflow: hidden;
    background: var(--paper);
    font-family: "Saira Condensed", sans-serif;
  }
  .hero-photo {
    position: absolute;
    left: 47px;
    top: 224px;
    width: 750px;
    height: 670px;
    background:
      radial-gradient(ellipse 26% 22% at 24% 14%, #8a847d 0%, #b3aea8 55%, rgba(235,232,227,0) 100%),
      linear-gradient(35deg, rgba(235,232,227,0) 45%, var(--steel-dark) 58%, #3a3633 74%, rgba(235,232,227,0) 88%),
      radial-gradient(ellipse 40% 34% at 24% 26%, var(--steel-light) 0%, rgba(235,232,227,0) 100%);
    -webkit-mask-image: radial-gradient(ellipse 70% 70% at 50% 50%, #000 55%, transparent 100%);
    mask-image: radial-gradient(ellipse 70% 70% at 50% 50%, #000 55%, transparent 100%);
    opacity: 0.85;
  }
  .date {
    position: absolute;
    left: 57px;
    top: 66px;
    margin: 0;
    font-size: 92px;
    font-weight: 500;
    line-height: 1;
    color: var(--coral);
    letter-spacing: 2px;
  }
  .hours {
    position: absolute;
    right: 56px;
    top: 82px;
    margin: 0;
    font-size: 19px;
    font-weight: 500;
    line-height: 22px;
    text-transform: uppercase;
    text-align: right;
    color: var(--ink);
  }
  .headline {
    position: absolute;
    left: 52px;
    top: 352px;
    margin: 0;
    font-size: 276px;
    font-weight: 500;
    line-height: 0.754;
    color: var(--coral);
    letter-spacing: 0;
    transform: scaleX(0.86);
    transform-origin: left top;
    white-space: nowrap;
  }
  .headline span { display: block; }
  .tagline {
    position: absolute;
    left: 55px;
    top: 870px;
    margin: 0;
    font-size: 84px;
    font-weight: 500;
    line-height: 1;
    color: var(--ink);
    transform: scaleX(0.7);
    transform-origin: left top;
    white-space: nowrap;
  }
  .rule {
    position: absolute;
    left: 55px;
    width: 326px;
    height: 4px;
    background: var(--ink);
  }
  .rule--one { top: 960px; }
  .rule--two { top: 1065px; }
  .rule--three { top: 1132px; }
  .description {
    position: absolute;
    left: 55px;
    top: 977px;
    width: 330px;
    margin: 0;
    font-size: 19px;
    font-weight: 500;
    line-height: 22px;
    text-transform: uppercase;
    color: var(--ink);
  }
  .contact {
    position: absolute;
    left: 56px;
    top: 1082px;
    margin: 0;
    font-family: "Arimo", sans-serif;
    font-size: 15px;
    line-height: 20px;
    color: var(--coral);
    white-space: nowrap;
  }
  .contact .web { font-weight: 700; }
  .brand-name {
    position: absolute;
    left: 560px;
    top: 1030px;
    margin: 0;
    font-size: 58px;
    font-weight: 500;
    line-height: 0.95;
    color: var(--tan);
    text-align: center;
  }
</style>
</head>
<body>
  <main class="flyer">
    <div class="hero-photo" role="img" aria-label="Photo of an espresso portafilter filled with ground coffee"></div>

    <p class="date">01/01/14</p>
    <p class="hours">Weekdays 7am – 6pm<br>Sat 8am – 3pm<br>Closed Sun &amp; PH</p>

    <h1 class="headline"><span>GRAND</span><span>OPENING</span></h1>

    <h2 class="tagline">BRAND NEW.</h2>
    <div class="rule rule--one"></div>
    <p class="description">Offering the largest &amp; finest selection of Italian, Colombian &amp; local coffees in Singapore's Central Business District.</p>
    <div class="rule rule--two"></div>
    <p class="contact">24 Brindlemere Wharf, The Linden Court #03-18<br><span class="web">www.kindlybrewed.com</span></p>
    <div class="rule rule--three"></div>

    <p class="brand-name">Kindly<br>Brewed</p>
  </main>
</body>
</html>
```